Business Cards for Logistics Company

Looking to update Business Card Design.
Logo is attached. Blue background is not a part of the logo, you can remove it in layers.

Company: Harbor Crest Freightways
Industry: Logistics, Container Shipping

Address:
418 Willow Bend Ave
Linden Cove RI 02908

Phones:
p. 401-555-3142
f. 401-555-3149
c. very by person's name

Website: www.hcfroute.example

Design has to include person's name and position.

Target Market(s)

B2B

Industry/Entity Type

Business

Contact Information for Business Card

Card Size (non standard): 1039 x 697 pixels, 300dpi

Font styles to use
Serif
Sans Serif

```html
<!DOCTYPE html>
<html lang="en">
<head>
<meta charset="utf-8">
<title>Harbor Crest Freightways – Business Card</title>
<link rel="stylesheet" href="https://fonts.googleapis.com/css2?family=Open+Sans:wght@400;600;700&display=swap">
<style>
  :root {
    --page-bg: #e9e9ec;
    --card-top: #101c45;
    --card-bottom: #24386f;
    --ink: #ffffff;
    --ink-soft: #e8ecf6;
    --mark-fill: #3f7fd0;
  }
  * { margin: 0; padding: 0; box-sizing: border-box; }
  html, body {
    width: 1200px; height: 900px; overflow: hidden;
    background: var(--page-bg);
    font-family: "Open Sans", Arial, sans-serif;
  }
  .card {
    position: absolute; left: 150px; top: 148px;
    width: 900px; height: 604px;
    border-radius: 20px;
    background: linear-gradient(180deg, var(--card-top) 0%, var(--card-bottom) 100%);
    color: var(--ink);
    box-shadow: 0 10px 30px rgba(10, 20, 50, 0.25);
  }
  .brand-mark {
    position: absolute; left: 160px; top: 88px;
    width: 190px; height: 190px;
    background: var(--mark-fill);
  }
  .brand-name {
    position: absolute; left: 390px; top: 140px;
    font-size: 34px; font-weight: 400; line-height: 40px;
    letter-spacing: 5px; text-transform: uppercase;
    color: var(--ink);
  }
  .person {
    position: absolute; right: 511px; top: 355px;
    text-align: right;
  }
  .person-name { font-size: 29px; font-weight: 700; line-height: 40px; }
  .person-title { font-size: 22px; font-weight: 400; line-height: 34px; color: var(--ink-soft); }
  .address { margin-top: 12px; font-size: 22px; line-height: 34px; color: var(--ink-soft); }
  .contacts {
    position: absolute; left: 483px; top: 364px;
    list-style: none;
  }
  .contacts li {
    display: flex; align-items: center;
    height: 37.5px; font-size: 22px; color: var(--ink-soft);
  }
  .contacts svg { width: 18px; height: 18px; margin-right: 24px; fill: var(--ink); }
</style>
</head>
<body>
  <main class="card">
    <div class="brand-mark" aria-hidden="true"></div>
    <div class="brand-name">Harbor Crest<br>Freightways</div>

    <section class="person">
      <div class="person-name">Dmitri Valenkov</div>
      <div class="person-title">General Manager</div>
      <div class="address">418 Willow Bend Ave<br>Linden Cove RI 02908</div>
    </section>

    <ul class="contacts">
      <li>
        <svg viewBox="0 0 24 24" aria-label="Phone"><path d="M6.6 10.8c1.4 2.8 3.8 5.1 6.6 6.6l2.2-2.2c.3-.3.7-.4 1-.2 1.1.4 2.3.6 3.6.6.6 0 1 .4 1 1V20c0 .6-.4 1-1 1C10.6 21 3 13.4 3 4c0-.6.4-1 1-1h3.5c.6 0 1 .4 1 1 0 1.3.2 2.5.6 3.6.1.3 0 .7-.2 1z"/></svg>
        401-555-3142
      </li>
      <li>
        <svg viewBox="0 0 24 24" aria-label="Fax"><path d="M7 2h8l3 3v5H7zM4 11h16a2 2 0 0 1 2 2v7a2 2 0 0 1-2 2H4a2 2 0 0 1-2-2v-7a2 2 0 0 1 2-2zm3 3v2h2v-2zm4 0v2h2v-2zm4 0v2h2v-2zm-8 4v2h2v-2zm4 0v2h2v-2zm4 0v2h2v-2z"/></svg>
        401-555-3149
      </li>
      <li>
        <svg viewBox="0 0 24 24" aria-label="Mobile"><path d="M7 1h10a2 2 0 0 1 2 2v18a2 2 0 0 1-2 2H7a2 2 0 0 1-2-2V3a2 2 0 0 1 2-2zm0 3v14h10V4zm5 15.5a1 1 0 1 0 0 2 1 1 0 0 0 0-2z"/></svg>
        401.555.0178
      </li>
      <li>
        <svg viewBox="0 0 24 24" aria-label="Email"><path d="M2 5h20v14H2zm2 2v.5l8 5 8-5V7zm0 3v7h16v-7l-8 5z"/></svg>
        dispatch@hcfroute.example
      </li>
    </ul>
  </main>
</body>
</html>
```